Design a Brochure for kids ski camps,husky outings and christmas present ideas

I need a brochure to publicise my ski camps,saturday winter camps,husky dog outings and xmas present ideas, all for kids aged 4-16 yeard old

I may be in traditional style or cartoon style with snow, mountains, husky dogs etc.

It'll have a cover with TRLVENTURES WINTER ACTIVITIES as a title

inside pages for ski school holidays day camps + same but with English lessons, Saturday ski school, Saturday ski and English camps, husky outings and xmas present ideas

You will need to leave space for the French version as well ( I will send text afterwards)

I will also need this in a format for my webpage and to insert into emails and each page could alos be used as a flyer in itself

All in all it will be 12 pages with a backgrond , some text and pictures

Check trlventures.example for logo details and http://www.trlventures.example/ski-day-camps-01st-5th-of-april.html

If you are able to put in a accordeon fold so that I can seperate English from French then please advise

regards

Gavin

PS You must be used to dealing with printers and their requirments, if you are not please do not apply

please leave space for some photos.

Fill in with some text aaaaaaaaaaaaaaaaaaaaaaaaaaaaaaaaa etc. I will pass on teh texts once we have a design that pleases my eye

There will be 3/4 other jobs

```html
<!DOCTYPE html>
<html lang="en">
<head>
<meta charset="utf-8">
<title>TRLVENTURES Winter Activities Brochure</title>
<link href="https://fonts.googleapis.com/css2?family=Arimo:wght@400;700&display=swap" rel="stylesheet">
<style>
:root{
  --sky:#29a9e1;
  --sky-deep:#1b8fcf;
  --ink:#ffffff;
  --paper:#ffffff;
  --snow:#e9eef2;
  --frame-yellow:#f5cf00;
  --frame-red:#e5252b;
  --frame-purple:#96509e;
  --frame-green:#66bb38;
  --frame-blue:#2aa7df;
  --band-1:#f29aa3;
  --band-2:#f7d98b;
  --band-3:#b7dea0;
  --band-4:#97d2ee;
  --band-5:#d7a7d8;
}
*{box-sizing:border-box;margin:0;padding:0}
html,body{width:1173px;height:1200px;overflow:hidden;background:var(--paper)}
body{font-family:"Arimo",Arial,sans-serif}
.canvas{position:relative;width:1173px;height:1200px;overflow:hidden;background:var(--paper)}
.spread{position:absolute;width:573px;height:390px;box-shadow:0 0 3px rgba(0,0,0,.15)}
.col-1{left:0}.col-2{left:600px}
.row-1{top:0}.row-2{top:405px}.row-3{top:810px}
.page{position:absolute;top:0;width:286.5px;height:390px;overflow:hidden;
  background:linear-gradient(to bottom,#fff 0%,#f7f9fa 55%,var(--snow) 100%)}
.page--a{left:0}
.page--b{left:286.5px}
.page--a::after{content:"";position:absolute;right:0;top:0;width:14px;height:100%;
  background:linear-gradient(to left,rgba(0,0,0,.08),transparent)}
.band{position:absolute;left:0;top:0;width:100%;height:118px;
  background:linear-gradient(90deg,var(--band-1),var(--band-2) 25%,var(--band-3) 50%,var(--band-4) 75%,var(--band-5))}
.band::after{content:"";position:absolute;inset:0;
  background:linear-gradient(to bottom,rgba(255,255,255,0) 15%,rgba(255,255,255,.7) 65%,#fff 100%)}
.page-title{position:absolute;top:32px;left:14px;right:14px;font-weight:700;font-size:15.5px;
  letter-spacing:.2px;color:var(--ink);text-shadow:0 1px 2px rgba(0,0,0,.18);white-space:nowrap}
.page--b .page-title{text-align:right}
.panels{position:absolute;left:0;top:0;width:286.5px;height:390px}
.page--b .panels{transform:scaleX(-1)}
.panels path{fill:var(--sky)}
.copy{position:absolute;color:var(--ink);font-size:5.3px;line-height:6.6px;overflow:hidden}
.copy p{margin-bottom:4px}
.copy .age{padding-left:8px}
.copy .age b{font-weight:400;margin-left:-8px}
.copy ul{list-style:none;padding-left:10px}
.copy li{position:relative}
.copy li::before{content:"";position:absolute;left:-6px;top:2px;width:2.5px;height:2.5px;border-radius:50%;background:var(--ink)}
.page--a .copy--top{left:19px;top:92px;width:106px;height:142px}
.page--b .copy--top{left:161px;top:92px;width:106px;height:142px}
.page--a .copy--bottom{left:148px;top:214px;width:126px;height:166px}
.page--b .copy--bottom{left:12px;top:214px;width:126px;height:166px}
.photo{position:absolute;border:4px solid var(--frame-blue);border-radius:9px;background:var(--fill);
  box-shadow:0 1px 3px rgba(0,0,0,.25)}
.frame-yellow{border-color:var(--frame-yellow)}
.frame-red{border-color:var(--frame-red)}
.frame-purple{border-color:var(--frame-purple)}
.frame-green{border-color:var(--frame-green)}
.frame-blue{border-color:var(--frame-blue)}
.page--a .photo--top{left:146px;top:80px;width:128px;height:94px;transform:rotate(1.5deg)}
.page--b .photo--top{left:12px;top:80px;width:128px;height:94px;transform:rotate(-1.5deg)}
.page--a .photo--bottom{left:12px;top:298px;width:122px;height:84px;transform:rotate(-1deg)}
.page--b .photo--bottom{left:152px;top:298px;width:122px;height:84px;transform:rotate(1deg)}
.contact{position:absolute;left:52px;top:120px;color:var(--sky);font-weight:700;font-size:12.5px;line-height:18px}
.meeting{position:absolute;left:52px;top:172px;color:var(--sky);font-weight:700;font-size:12.5px;line-height:18px}
.meeting ul{list-style:none;position:absolute;left:137px;top:0;white-space:nowrap}
.snowfield{position:absolute;left:0;right:0;top:230px;height:90px;
  background:linear-gradient(to bottom,rgba(255,255,255,0),#e4e9ee 60%,#f1f4f6)}
.brand{position:absolute;left:52px;top:338px;display:flex;align-items:center;gap:6px}
.page--b .brand{left:40px}
.brand-mark{width:7px;height:7px;background:var(--frame-red)}
.brand-name{font-weight:700;font-size:22px;color:var(--sky);letter-spacing:.5px}
.brand-bar{position:absolute;left:52px;top:372px;width:170px;height:6px;background:var(--sky)}
.page--b .brand-bar{left:40px;width:180px}
.collage .photo{transform:none}
.c1{left:6px;top:128px;width:126px;height:94px;transform:rotate(-2deg)!important}
.c2{left:144px;top:92px;width:124px;height:66px;transform:rotate(2deg)!important}
.c3{left:10px;top:234px;width:124px;height:92px;transform:rotate(2deg)!important}
.c4{left:144px;top:206px;width:126px;height:88px;transform:rotate(-2deg)!important}
</style>
</head>
<body>
<main class="canvas">

<!-- Cover spread -->
<article class="spread col-1 row-1">
  <section class="page page--a">
    <div class="band"></div>
    <div class="snowfield"></div>
    <div class="contact">info@trlventures.example<br>+41(0)00.555.01.23</div>
    <div class="meeting">Meeting Points :
      <ul><li>CENTRE</li><li>LAKESIDE</li><li>HILLTOP</li></ul>
    </div>
    <div class="brand"><span class="brand-mark"></span><span class="brand-name">TRLVENTURES</span></div>
    <div class="brand-bar"></div>
  </section>
  <section class="page page--b collage">
    <div class="band"></div>
    <div class="snowfield"></div>
    <div class="photo frame-yellow c1" role="img" aria-label="Child skiing on a snowy slope" style="--fill:linear-gradient(160deg,#c9dff0,#f3f6f8 60%,#5a7fb0)"></div>
    <div class="photo frame-red c2" role="img" aria-label="Children playing at the beach" style="--fill:linear-gradient(160deg,#7fc4ea,#e9c89a 60%,#d88a6a)"></div>
    <div class="photo frame-purple c3" role="img" aria-label="Child at a crafts table" style="--fill:linear-gradient(160deg,#c57b5a,#e6b58a 50%,#7aa0c8)"></div>
    <div class="photo frame-green c4" role="img" aria-label="Child with headphones at a computer" style="--fill:linear-gradient(160deg,#e6e6ea,#9fb0c4 55%,#3b4d66)"></div>
    <div class="brand"><span class="brand-mark"></span><span class="brand-name">TRLVENTURES</span></div>
    <div class="brand-bar"></div>
  </section>
</article>

<!-- Holiday day camp / Winter camp -->
<article class="spread col-2 row-1">
  <section class="page page--a">
    <div class="band"></div>
    <h2 class="page-title">HOLIDAY DAY CAMP</h2>
    <svg class="panels" viewBox="0 0 286 390" aria-hidden="true"><path d="M14 92 Q14 86 20 86 H124 Q130 86 130 92 V236 Q72 254 14 236 Z"/><path d="M0 300 C40 262 90 208 150 200 C200 194 250 196 286 206 V390 H0 Z"/></svg>
    <div class="copy copy--top"><p>Holiday day camp is organized by trlventures with intention to spread smile on children's face.</p><p class="age"><b>Age Group</b><br>Minis ( 4-6 years)<br>Kids ( 7 - 10 years)<br>Teens ( 11 - 16 years)</p><p>We take good care of your children when we pick them up at the CENTRE, LAKESIDE and HILLTOP, and during the whole day. We drive them by bus to each activity in the region, and drop them back at the meeting point. We are careful about not having more than 8 children per monitor, to provide an optimal supervision. Every monitor is qualified and experienced. It's all Fun and safe!</p><ul><li>680chf for 5 days including transport, activities and tuition</li><li>Parents must provide a packed lunch and snacks</li></ul></div>
    <div class="photo photo--top frame-blue" role="img" aria-label="Children running through a wheat field" style="--fill:linear-gradient(to bottom,#8cc3ea 0%,#bcd9ee 35%,#d8b86a 45%,#b58a3c 100%)"></div>
    <div class="copy copy--bottom"><p>Holiday day camp is organized by trlventures with intention to spread smile on children's face.</p><p class="age"><b>Age Group</b><br>Minis ( 4-6 years)<br>Kids ( 7 - 10 years)<br>Teens ( 11 - 16 years)</p><p>We take good care of your children when we pick them up at the CENTRE, LAKESIDE and HILLTOP, and during the whole day. We drive them by bus to each activity in the region, and drop them back at the meeting point. We are careful about not having more than 8 children per monitor, to provide an optimal supervision. Every monitor is qualified and experienced. It's all Fun and safe!</p><ul><li>680chf for 5 days including transport, activities and tuition</li><li>Parents must provide a packed lunch and snacks</li></ul></div>
    <div class="photo photo--bottom frame-purple" role="img" aria-label="Children racing on a running track" style="--fill:linear-gradient(160deg,#c9674c,#e0957a 55%,#7aa35a)"></div>
  </section>
  <section class="page page--b">
    <div class="band"></div>
    <h2 class="page-title">WINTER CAMP</h2>
    <svg class="panels" viewBox="0 0 286 390" aria-hidden="true"><path d="M14 92 Q14 86 20 86 H124 Q130 86 130 92 V236 Q72 254 14 236 Z"/><path d="M0 300 C40 262 90 208 150 200 C200 194 250 196 286 206 V390 H0 Z"/></svg>
    <div class="copy copy--top"><p>Winter camp is organized by trlventures with intention to spread smile on children's face.</p><p class="age"><b>Age Group</b><br>Minis ( 4-6 years)<br>Kids ( 7 - 10 years)<br>Teens ( 11 - 16 years)</p><p>We take good care of your children when we pick them up at the CENTRE, LAKESIDE and HILLTOP, and during the whole day. We drive them by bus to each activity in the region, and drop them back at the meeting point. We are careful about not having more than 8 children per monitor, to provide an optimal supervision. Every monitor is qualified and experienced. It's all Fun and safe!</p><ul><li>680chf for 5 days including transport, activities and tuition</li><li>Parents must provide a packed lunch and snacks</li></ul></div>
    <div class="photo photo--top frame-red" role="img" aria-label="Children skiing on a snowy slope" style="--fill:linear-gradient(160deg,#f4f6f8,#dfe6ec 60%,#8a9aae)"></div>
    <div class="copy copy--bottom"><p>Winter camp is organized by trlventures with intention to spread smile on children's face.</p><p class="age"><b>Age Group</b><br>Minis ( 4-6 years)<br>Kids ( 7 - 10 years)<br>Teens ( 11 - 16 years)</p><p>We take good care of your children when we pick them up at the CENTRE, LAKESIDE and HILLTOP, and during the whole day. We drive them by bus to each activity in the region, and drop them back at the meeting point. We are careful about not having more than 8 children per monitor, to provide an optimal supervision. Every monitor is qualified and experienced. It's all Fun and safe!</p><ul><li>680chf for 5 days including transport, activities and tuition</li><li>Parents must provide a packed lunch and snacks</li></ul></div>
    <div class="photo photo--bottom frame-green" role="img" aria-label="Child inside a snow cave" style="--fill:radial-gradient(circle at 50% 55%,#7fb2d8,#24415f 70%)"></div>
  </section>
</article>

<!-- Husky dog outing / Saturday winter camp -->
<article class="spread col-1 row-2">
  <section class="page page--a">
    <div class="band"></div>
    <h2 class="page-title">HUSKY DOG OUTING</h2>
    <svg class="panels" viewBox="0 0 286 390" aria-hidden="true"><path d="M14 92 Q14 86 20 86 H124 Q130 86 130 92 V236 Q72 254 14 236 Z"/><path d="M0 300 C40 262 90 208 150 200 C200 194 250 196 286 206 V390 H0 Z"/></svg>
    <div class="copy copy--top"><p>Husky dog outing is organized by trlventures with intention to spread smile on children's face.</p><p class="age"><b>Age Group</b><br>Minis ( 4-6 years)<br>Kids ( 7 - 10 years)<br>Teens ( 11 - 16 years)</p><p>We take good care of your children when we pick them up at the CENTRE, LAKESIDE and HILLTOP, and during the whole day. We drive them by bus to each activity in the region, and drop them back at the meeting point. We are careful about not having more than 8 children per monitor, to provide an optimal supervision. Every monitor is qualified and experienced. It's all Fun and safe!</p><ul><li>680chf for 5 days including transport, activities and tuition</li><li>Parents must provide a packed lunch and snacks</li></ul></div>
    <div class="photo photo--top frame-yellow" role="img" aria-label="Girl hugging a husky dog" style="--fill:linear-gradient(160deg,#6b4a2e,#b08a62 50%,#e3d4c2)"></div>
    <div class="copy copy--bottom"><p>Husky dog outing is organized by trlventures with intention to spread smile on children's face.</p><p class="age"><b>Age Group</b><br>Minis ( 4-6 years)<br>Kids ( 7 - 10 years)<br>Teens ( 11 - 16 years)</p><p>We take good care of your children when we pick them up at the CENTRE, LAKESIDE and HILLTOP, and during the whole day. We drive them by bus to each activity in the region, and drop them back at the meeting point. We are careful about not having more than 8 children per monitor, to provide an optimal supervision. Every monitor is qualified and experienced. It's all Fun and safe!</p><ul><li>680chf for 5 days including transport, activities and tuition</li><li>Parents must provide a packed lunch and snacks</li></ul></div>
    <div class="photo photo--bottom frame-purple" role="img" aria-label="Husky dog lying in the snow" style="--fill:linear-gradient(160deg,#f1f3f5,#b9c2cc 50%,#4b4f56)"></div>
  </section>
  <section class="page page--b">
    <div class="band"></div>
    <h2 class="page-title">SATURDAY WINTER CAMP</h2>
    <svg class="panels" viewBox="0 0 286 390" aria-hidden="true"><path d="M14 92 Q14 86 20 86 H124 Q130 86 130 92 V236 Q72 254 14 236 Z"/><path d="M0 300 C40 262 90 208 150 200 C200 194 250 196 286 206 V390 H0 Z"/></svg>
    <div class="copy copy--top"><p>Saturday winter camp is organized by trlventures with intention to spread smile on children's face.</p><p class="age"><b>Age Group</b><br>Minis ( 4-6 years)<br>Kids ( 7 - 10 years)<br>Teens ( 11 - 16 years)</p><p>We take good care of your children when we pick them up at the CENTRE, LAKESIDE and HILLTOP, and during the whole day. We drive them by bus to each activity in the region, and drop them back at the meeting point. We are careful about not having more than 8 children per monitor, to provide an optimal supervision. Every monitor is qualified and experienced. It's all Fun and safe!</p><ul><li>680chf for 5 days including transport, activities and tuition</li><li>Parents must provide a packed lunch and snacks</li></ul></div>
    <div class="photo photo--top frame-red" role="img" aria-label="Boy reading a map" style="--fill:linear-gradient(160deg,#d9e3ea,#e9c9a8 50%,#c05a3c)"></div>
    <div class="copy copy--bottom"><p>Saturday winter camp is organized by trlventures with intention to spread smile on children's face.</p><p class="age"><b>Age Group</b><br>Minis ( 4-6 years)<br>Kids ( 7 - 10 years)<br>Teens ( 11 - 16 years)</p><p>We take good care of your children when we pick them up at the CENTRE, LAKESIDE and HILLTOP, and during the whole day. We drive them by bus to each activity in the region, and drop them back at the meeting point. We are careful about not having more than 8 children per monitor, to provide an optimal supervision. Every monitor is qualified and experienced. It's all Fun and safe!</p><ul><li>680chf for 5 days including transport, activities and tuition</li><li>Parents must provide a packed lunch and snacks</li></ul></div>
    <div class="photo photo--bottom frame-green" role="img" aria-label="Young child playing with toys" style="--fill:linear-gradient(160deg,#f3efe6,#e8c090 55%,#d67a2e)"></div>
  </section>
</article>

<!-- English lesson camps / Saturday English lessons -->
<article class="spread col-2 row-2">
  <section class="page page--a">
    <div class="band"></div>
    <h2 class="page-title">ENGLISH LESSON CAMPS</h2>
    <svg class="panels" viewBox="0 0 286 390" aria-hidden="true"><path d="M14 92 Q14 86 20 86 H124 Q130 86 130 92 V236 Q72 254 14 236 Z"/><path d="M0 300 C40 262 90 208 150 200 C200 194 250 196 286 206 V390 H0 Z"/></svg>
    <div class="copy copy--top"><p>English lesson camp is organized by trlventures with intention to spread smile on children's face.</p><p class="age"><b>Age Group</b><br>Minis ( 4-6 years)<br>Kids ( 7 - 10 years)<br>Teens ( 11 - 16 years)</p><p>We take good care of your children when we pick them up at the CENTRE, LAKESIDE and HILLTOP, and during the whole day. We drive them by bus to each activity in the region, and drop them back at the meeting point. We are careful about not having more than 8 children per monitor, to provide an optimal supervision. Every monitor is qualified and experienced. It's all Fun and safe!</p><ul><li>680chf for 5 days including transport, activities and tuition</li><li>Parents must provide a packed lunch and snacks</li></ul></div>
    <div class="photo photo--top frame-blue" role="img" aria-label="Children in a classroom" style="--fill:linear-gradient(160deg,#f2ede2,#d9c6a6 50%,#8f6c4a)"></div>
    <div class="copy copy--bottom"><p>English lesson camp is organized by trlventures with intention to spread smile on children's face.</p><p class="age"><b>Age Group</b><br>Minis ( 4-6 years)<br>Kids ( 7 - 10 years)<br>Teens ( 11 - 16 years)</p><p>We take good care of your children when we pick them up at the CENTRE, LAKESIDE and HILLTOP, and during the whole day. We drive them by bus to each activity in the region, and drop them back at the meeting point. We are careful about not having more than 8 children per monitor, to provide an optimal supervision. Every monitor is qualified and experienced. It's all Fun and safe!</p><ul><li>680chf for 5 days including transport, activities and tuition</li><li>Parents must provide a packed lunch and snacks</li></ul></div>
    <div class="photo photo--bottom frame-blue" role="img" aria-label="Children reading together at a desk" style="--fill:linear-gradient(160deg,#e9e6df,#c98f6a 55%,#3f6fa8)"></div>
  </section>
  <section class="page page--b">
    <div class="band"></div>
    <h2 class="page-title">SATURDAY ENGLISH LESSONS</h2>
    <svg class="panels" viewBox="0 0 286 390" aria-hidden="true"><path d="M14 92 Q14 86 20 86 H124 Q130 86 130 92 V236 Q72 254 14 236 Z"/><path d="M0 300 C40 262 90 208 150 200 C200 194 250 196 286 206 V390 H0 Z"/></svg>
    <div class="copy copy--top"><p>Saturday English lessons are organized by trlventures with intention to spread smile on children's face.</p><p class="age"><b>Age Group</b><br>Minis ( 4-6 years)<br>Kids ( 7 - 10 years)<br>Teens ( 11 - 16 years)</p><p>We take good care of your children when we pick them up at the CENTRE, LAKESIDE and HILLTOP, and during the whole day. We drive them by bus to each activity in the region, and drop them back at the meeting point. We are careful about not having more than 8 children per monitor, to provide an optimal supervision. Every monitor is qualified and experienced. It's all Fun and safe!</p><ul><li>680chf for 5 days including transport, activities and tuition</li><li>Parents must provide a packed lunch and snacks</li></ul></div>
    <div class="photo photo--top frame-red" role="img" aria-label="Children at a green chalkboard" style="--fill:linear-gradient(160deg,#2f6a4a,#5c8f6e 50%,#e6cba6)"></div>
    <div class="copy copy--bottom"><p>Saturday English lessons are organized by trlventures with intention to spread smile on children's face.</p><p class="age"><b>Age Group</b><br>Minis ( 4-6 years)<br>Kids ( 7 - 10 years)<br>Teens ( 11 - 16 years)</p><p>We take good care of your children when we pick them up at the CENTRE, LAKESIDE and HILLTOP, and during the whole day. We drive them by bus to each activity in the region, and drop them back at the meeting point. We are careful about not having more than 8 children per monitor, to provide an optimal supervision. Every monitor is qualified and experienced. It's all Fun and safe!</p><ul><li>680chf for 5 days including transport, activities and tuition</li><li>Parents must provide a packed lunch and snacks</li></ul></div>
    <div class="photo photo--bottom frame-green" role="img" aria-label="Children raising hands in class" style="--fill:linear-gradient(160deg,#f0ece4,#9ec4e6 50%,#d0503c)"></div>
  </section>
</article>

<!-- Workshops / Xmas gift ideas -->
<article class="spread col-1 row-3">
  <section class="page page--a">
    <div class="band"></div>
    <h2 class="page-title">WORKSHOPS</h2>
    <svg class="panels" viewBox="0 0 286 390" aria-hidden="true"><path d="M14 92 Q14 86 20 86 H124 Q130 86 130 92 V236 Q72 254 14 236 Z"/><path d="M0 300 C40 262 90 208 150 200 C200 194 250 196 286 206 V390 H0 Z"/></svg>
    <div class="copy copy--top"><p>Various workshops are organized by trlventures with intention to spread smile on children's face.</p><p class="age"><b>Age Group</b><br>Minis ( 4-6 years)<br>Kids ( 7 - 10 years)<br>Teens ( 11 - 16 years)</p><p>We take good care of your children when we pick them up at the CENTRE, LAKESIDE and HILLTOP, and during the whole day. We drive them by bus to each activity in the region, and drop them back at the meeting point. We are careful about not having more than 8 children per monitor, to provide an optimal supervision. Every monitor is qualified and experienced. It's all Fun and safe!</p><ul><li>680chf for 5 days including transport, activities and tuition</li><li>Parents must provide a packed lunch and snacks</li></ul></div>
    <div class="photo photo--top frame-yellow" role="img" aria-label="Child painting outdoors on grass" style="--fill:linear-gradient(160deg,#9ccf6a,#5fa03e 55%,#2f6a2a)"></div>
    <div class="copy copy--bottom"><p>Various workshops are organized by trlventures with intention to spread smile on children's face.</p><p class="age"><b>Age Group</b><br>Minis ( 4-6 years)<br>Kids ( 7 - 10 years)<br>Teens ( 11 - 16 years)</p><p>We take good care of your children when we pick them up at the CENTRE, LAKESIDE and HILLTOP, and during the whole day. We drive them by bus to each activity in the region, and drop them back at the meeting point. We are careful about not having more than 8 children per monitor, to provide an optimal supervision. Every monitor is qualified and experienced. It's all Fun and safe!</p><ul><li>680chf for 5 days including transport, activities and tuition</li><li>Parents must provide a packed lunch and snacks</li></ul></div>
    <div class="photo photo--bottom frame-purple" role="img" aria-label="Children playing with building blocks" style="--fill:linear-gradient(160deg,#f2c84a,#e2603a 50%,#3d86c6)"></div>
  </section>
  <section class="page page--b">
    <div class="band"></div>
    <h2 class="page-title">X'MAS GIFT IDEAS</h2>
    <svg class="panels" viewBox="0 0 286 390" aria-hidden="true"><path d="M14 92 Q14 86 20 86 H124 Q130 86 130 92 V236 Q72 254 14 236 Z"/><path d="M0 300 C40 262 90 208 150 200 C200 194 250 196 286 206 V390 H0 Z"/></svg>
    <div class="copy copy--top"><p>X'mas gift event is organized by trlventures with intention to spread smile on children's face.</p><p class="age"><b>Age Group</b><br>Minis ( 4-6 years)<br>Kids ( 7 - 10 years)<br>Teens ( 11 - 16 years)</p><p>We take good care of your children when we pick them up at the CENTRE, LAKESIDE and HILLTOP, and during the whole day. We drive them by bus to each activity in the region, and drop them back at the meeting point. We are careful about not having more than 8 children per monitor, to provide an optimal supervision. Every monitor is qualified and experienced. It's all Fun and safe!</p><ul><li>680chf for 5 days including transport, activities and tuition</li><li>Parents must provide a packed lunch and snacks</li></ul></div>
    <div class="photo photo--top frame-red" role="img" aria-label="Snowman decoration on a dark background" style="--fill:radial-gradient(circle at 50% 50%,#e9eef3 0,#9aa6b4 30%,#141a24 70%)"></div>
    <div class="copy copy--bottom"><p>X'mas gift event is organized by trlventures with intention to spread smile on children's face.</p><p class="age"><b>Age Group</b><br>Minis ( 4-6 years)<br>Kids ( 7 - 10 years)<br>Teens ( 11 - 16 years)</p><p>We take good care of your children when we pick them up at the CENTRE, LAKESIDE and HILLTOP, and during the whole day. We drive them by bus to each activity in the region, and drop them back at the meeting point. We are careful about not having more than 8 children per monitor, to provide an optimal supervision. Every monitor is qualified and experienced. It's all Fun and safe!</p><ul><li>680chf for 5 days including transport, activities and tuition</li><li>Parents must provide a packed lunch and snacks</li></ul></div>
    <div class="photo photo--bottom frame-green" role="img" aria-label="Red wrapped gift box with gold ribbon" style="--fill:radial-gradient(circle at 50% 45%,#e23a2e,#a0121a 70%)"></div>
  </section>
</article>

<!-- Program benefits / At a glance -->
<article class="spread col-2 row-3">
  <section class="page page--a">
    <div class="band"></div>
    <h2 class="page-title">PROGRAM BENEFITS</h2>
    <svg class="panels" viewBox="0 0 286 390" aria-hidden="true"><path d="M14 92 Q14 86 20 86 H124 Q130 86 130 92 V236 Q72 254 14 236 Z"/><path d="M0 300 C40 262 90 208 150 200 C200 194 250 196 286 206 V390 H0 Z"/></svg>
    <div class="copy copy--top"><p>Main intention of program is to develop children's personality and provide them exclusive environment.</p><p class="age"><b>Age Group</b><br>Minis ( 4-6 years)<br>Kids ( 7 - 10 years)<br>Teens ( 11 - 16 years)</p><p>We take good care of your children when we pick them up at the CENTRE, LAKESIDE and HILLTOP, and during the whole day. We drive them by bus to each activity in the region, and drop them back at the meeting point. We are careful about not having more than 8 children per monitor, to provide an optimal supervision. Every monitor is qualified and experienced. It's all Fun and safe!</p><ul><li>680chf for 5 days including transport, activities and tuition</li><li>Parents must provide a packed lunch and snacks</li></ul></div>
    <div class="photo photo--top frame-yellow" role="img" aria-label="Child on inline skates with a helmet" style="--fill:linear-gradient(160deg,#dfe6ec,#9aa3ad 55%,#5d6670)"></div>
    <div class="copy copy--bottom"><p>Main intention of program is to develop children's personality and provide them exclusive environment.</p><p class="age"><b>Age Group</b><br>Minis ( 4-6 years)<br>Kids ( 7 - 10 years)<br>Teens ( 11 - 16 years)</p><p>We take good care of your children when we pick them up at the CENTRE, LAKESIDE and HILLTOP, and during the whole day. We drive them by bus to each activity in the region, and drop them back at the meeting point. We are careful about not having more than 8 children per monitor, to provide an optimal supervision. Every monitor is qualified and experienced. It's all Fun and safe!</p><ul><li>680chf for 5 days including transport, activities and tuition</li><li>Parents must provide a packed lunch and snacks</li></ul></div>
    <div class="photo photo--bottom frame-purple" role="img" aria-label="Group of children ice skating" style="--fill:linear-gradient(160deg,#eef2f5,#c7d2dc 55%,#7e8c9a)"></div>
  </section>
  <section class="page page--b">
    <div class="band"></div>
    <h2 class="page-title">AT A GLANCE</h2>
    <svg class="panels" viewBox="0 0 286 390" aria-hidden="true"><path d="M14 92 Q14 86 20 86 H124 Q130 86 130 92 V236 Q72 254 14 236 Z"/><path d="M0 300 C40 262 90 208 150 200 C200 194 250 196 286 206 V390 H0 Z"/></svg>
    <div class="copy copy--top"><p>Our complete activities at a glance.</p><p class="age"><b>Age Group</b><br>Minis ( 4-6 years)<br>Kids ( 7 - 10 years)<br>Teens ( 11 - 16 years)</p><p>We take good care of your children when we pick them up at the CENTRE, LAKESIDE and HILLTOP, and during the whole day. We drive them by bus to each activity in the region, and drop them back at the meeting point. We are careful about not having more than 8 children per monitor, to provide an optimal supervision. Every monitor is qualified and experienced. It's all Fun and safe!</p><ul><li>680chf for 5 days including transport, activities and tuition</li><li>Parents must provide a packed lunch and snacks</li></ul></div>
    <div class="photo photo--top frame-red" role="img" aria-label="Child climbing a playground frame" style="--fill:linear-gradient(160deg,#cfd8e0,#8f9aa6 55%,#4a5562)"></div>
    <div class="copy copy--bottom"><p>Our complete activities at a glance.</p><p class="age"><b>Age Group</b><br>Minis ( 4-6 years)<br>Kids ( 7 - 10 years)<br>Teens ( 11 - 16 years)</p><p>We take good care of your children when we pick them up at the CENTRE, LAKESIDE and HILLTOP, and during the whole day. We drive them by bus to each activity in the region, and drop them back at the meeting point. We are careful about not having more than 8 children per monitor, to provide an optimal supervision. Every monitor is qualified and experienced. It's all Fun and safe!</p><ul><li>680chf for 5 days including transport, activities and tuition</li><li>Parents must provide a packed lunch and snacks</li></ul></div>
    <div class="photo photo--bottom frame-green" role="img" aria-label="Child playing on a green field" style="--fill:linear-gradient(160deg,#8fcf5a,#4f9a34 55%,#2c5e22)"></div>
  </section>
</article>

</main>
</body>
</html>
```